Fruits and Vegetables distribution company needs a new eye catching website

We need to get our website up to date. Our clients will look at our website to learn about our products and services. Our design needs to be simple yet impactful to make our brand memorable to our visitors. We need to have somewhere to tell our clients about our history, products and services, our team. We can throw in a few fun facts and figures and maybe some testimonials to impress. We have 4 theme colors that we want to incorporate into the design, you can get in touch for the HEX/RGB codes. Please remember that smooth operation of any animations and interactions is very important.

```html
<!DOCTYPE html>
<html lang="en">
<head>
<meta charset="utf-8">
<title>Bustana – Media Coverage</title>
<link href="https://fonts.googleapis.com/css2?family=Tenor+Sans&family=Jost:wght@400;500;600&display=swap" rel="stylesheet">
<style>
:root{
  --green:#8dc63f;
  --red:#c1272d;
  --yellow:#f5b819;
  --ink:#1a1a1a;
  --text:#666;
  --black:#111;
  --line:#e3e3e3;
  --sky:#1da1e2;
  --head:"Tenor Sans", sans-serif;
  --body:"Jost", sans-serif;
}
*{box-sizing:border-box;margin:0;padding:0}
html,body{width:673px;height:1200px;overflow:hidden;background:#fff}
.page{position:relative;width:673px;height:1200px;overflow:hidden;font-family:var(--body);color:var(--ink)}
.abs{position:absolute}

/* header */
.topline{font-size:9px;letter-spacing:.5px;display:flex;align-items:center;gap:6px}
.badge{width:18px;height:18px;border-radius:50%;border:1px solid #f3e3b0;display:flex;align-items:center;justify-content:center}
.social-dot{width:14px;height:14px;border-radius:50%;background:var(--yellow)}
.nav{top:39px;font-size:7.5px;font-weight:500;letter-spacing:.2px}
.nav.active{color:var(--green)}
.brand-box{left:298px;top:0;width:76px;height:74px;background:#fff;box-shadow:0 2px 5px rgba(0,0,0,.15);display:flex;flex-direction:column;align-items:center;justify-content:center;gap:6px;z-index:2}
.brand-mark{width:22px;height:22px;border-radius:50%;background:var(--red)}
.brand-name{font-family:var(--head);font-size:10px;letter-spacing:1.5px;color:#333}

/* hero */
.hero{left:0;top:59px;width:673px;height:159px;background:linear-gradient(100deg,#3d5a2a 0%,#b3261c 25%,#6b4a2e 50%,#d08a1c 65%,#3b2f3a 85%,#4b6e2c 100%)}
.hero-shade{position:absolute;inset:0;background:rgba(0,0,0,.3)}
.hero-title{position:absolute;left:0;right:0;top:70px;text-align:center;color:#fff;font-family:var(--head);font-size:16px;letter-spacing:.8px}

/* breadcrumb */
.crumbs{left:79px;top:223px;font-size:6.5px;color:#777;display:flex;gap:8px;align-items:center}
.crumbs .current{color:var(--green)}
.rule{left:0;top:238px;width:673px;height:1px;background:var(--line)}

/* section titles */
.section-title{left:0;width:673px;text-align:center;font-family:var(--head);font-size:15px;letter-spacing:.5px}
.divider{left:256px;width:161px;height:12px;display:flex;align-items:center;gap:6px}
.divider span{flex:1;height:1px;background:#555}
.lead{left:0;top:322px;width:673px;text-align:center;font-size:6.5px;color:#555}

/* coverage list */
.story-thumb{left:80px;width:106px;height:74px;border:3px solid #fff;box-shadow:0 0 3px rgba(0,0,0,.3)}
.date-day{position:absolute;left:0;top:0;background:var(--green);color:#fff;font-size:5.5px;padding:2px 3px;width:24px}
.date-year{position:absolute;left:0;top:13px;background:#3a3a3a;color:#fff;font-size:5.5px;padding:2px 3px;width:24px}
.story-body{left:197px;width:345px}
.story-title{font-size:7.2px;font-weight:500;margin-bottom:5px}
.story-text{font-size:5.4px;line-height:10px;color:var(--text)}

/* social */
.channel{top:690px;font-family:var(--head);font-size:10px;display:flex;align-items:center;gap:4px}
.channel i{display:block;width:8px;height:8px;background:var(--ink)}
.fb-box{left:80px;top:708px;width:118px;height:118px;border:1px solid #bbb;font-size:4.3px;line-height:5.2px;color:#333}
.fb-head{background:#eceef4;border-bottom:1px solid #ccc;padding:3px 3px;font-weight:600;font-size:5px}
.fb-item{display:flex;gap:3px;padding:3px 3px 0}
.fb-thumb{width:12px;height:12px;flex:none;background:#5a6f5a}
.fb-item b{color:#2c4a8a;font-weight:500}
.fb-foot{position:absolute;left:3px;right:3px;bottom:2px;border-top:1px solid #ccc;padding-top:2px;color:#555}
.ig-profile{left:289px;top:709px;width:100px;display:flex;gap:4px;font-size:4.5px;line-height:5.4px;color:#999}
.ig-avatar{width:20px;height:20px;border-radius:50%;background:#1e4a80;flex:none}
.ig-handle{color:#888;font-size:6px}
.ig-grid{left:289px;top:760px;width:93px;height:115px;display:grid;grid-template-columns:repeat(4,20px);grid-auto-rows:20px;gap:4px}
.ig-grid div{border:1px solid #fff;box-shadow:0 0 1.5px rgba(0,0,0,.4)}
.load-more{left:314px;top:881px;width:41px;height:12px;background:#333;color:#fff;font-size:4.8px;text-align:center;line-height:12px;border-radius:1px}
.tw-box{left:479px;top:706px;width:115px;height:155px;border:1px solid #9fd0ec;background:#eaf6fc}
.tw-head{background:var(--sky);color:#fff;font-size:5px;height:15px;padding:0 5px;display:flex;align-items:center;justify-content:space-between}
.tw-head i{display:block;width:7px;height:7px;background:#fff;border-radius:50%}
.tw-item{margin:2px 1px 0;padding:3px 3px;border-bottom:1px solid #9fd0ec;font-size:3.8px;line-height:4.6px;color:#333;height:33px;position:relative}
.tw-item::before{content:"";position:absolute;left:5px;top:5px;width:5px;height:5px;border-radius:50%;background:var(--sky)}
.tw-item p{padding-left:14px}
.tw-item .view{position:absolute;right:5px;bottom:3px;color:var(--sky)}

/* footer */
.footer{left:0;top:936px;width:673px;height:240px;background:var(--black)}
.foot-title{font-family:var(--head);color:#fff;font-size:12.5px;letter-spacing:.6px}
.foot-rule{height:1px;background:#444;width:121px}
.foot-line{color:#fff;font-size:6.5px;line-height:8.5px;display:flex;gap:10px;align-items:flex-start}
.foot-line svg{flex:none}
.follow-dot{width:9px;height:9px;border-radius:50%;background:#fff}
.touch{left:238px;top:930px;width:197px;height:222px;background:var(--green);padding:42px 16px 0}
.touch::before{content:"";position:absolute;top:0;left:-6px;border-style:solid;border-width:0 6px 6px 0;border-color:transparent #5e8a22 transparent transparent}
.touch h3{font-family:var(--head);font-weight:400;color:#fff;font-size:12.5px;letter-spacing:.6px}
.touch .foot-rule{background:#b9dd8a;width:166px;margin:8px 0 9px}
.field{background:#fff;height:17px;margin-bottom:7px;font-size:6px;color:#555;padding:5px 6px}
.field.tall{height:37px}
.submit{border:1px solid #fff;height:17px;color:#fff;font-size:7px;text-align:center;line-height:15px;letter-spacing:.5px}
.foot-brand{left:455px;top:980px;width:145px;display:flex;flex-direction:column;align-items:center;gap:14px}
.foot-brand .brand-mark{width:58px;height:58px}
.foot-brand .brand-name{color:#fff;font-size:20px;letter-spacing:3px}
.copybar{left:0;top:1176px;width:673px;height:24px;background:var(--red);color:#fff;font-size:6.5px;text-align:center;line-height:24px}
</style>
</head>
<body>
<div class="page">

  <!-- header -->
  <div class="abs topline" style="left:80px;top:5px">
    <span class="badge"><svg width="8" height="6" viewBox="0 0 8 6"><rect width="8" height="6" rx="1" fill="#f5b819"/><path d="M0 0 4 3.5 8 0" stroke="#fff" stroke-width=".8" fill="none"/></svg></span>
    info@bustana.com
  </div>
  <div class="abs topline" style="left:418px;top:5px">
    <span class="badge"><svg width="8" height="8" viewBox="0 0 8 8"><path d="M1.5 0.5 3 0.5 3.6 2.5 2.6 3.3C3.2 4.6 3.9 5.3 4.8 5.6L5.6 4.6 7.5 5.2 7.5 6.8C4 7.2.8 4 1.5.5Z" fill="#f5b819"/></svg></span>
    123-456-7890
  </div>
  <div class="abs social-dot" style="left:516px;top:7px" aria-label="Chirper"></div>
  <div class="abs social-dot" style="left:537px;top:7px" aria-label="Friendline"></div>
  <div class="abs social-dot" style="left:558px;top:7px" aria-label="Network"></div>
  <div class="abs social-dot" style="left:579px;top:7px" aria-label="Snapgrid"></div>

  <svg class="abs" style="left:79px;top:38px" width="10" height="9" viewBox="0 0 10 9"><path d="M5 0 10 4.5H8.6V9H6V6H4V9H1.4V4.5H0Z" fill="#1a1a1a"/></svg>
  <div class="abs nav" style="left:108px">OUR HISTORY</div>
  <div class="abs nav" style="left:177px">DIVISIONS</div>
  <div class="abs nav" style="left:238px">PRODUCT</div>
  <div class="abs nav" style="left:397px">SERVICES</div>
  <div class="abs nav active" style="left:461px">MEDIA COVERAGE</div>
  <div class="abs nav" style="left:557px">CONTACT</div>

  <div class="abs brand-box">
    <span class="brand-mark"></span>
    <span class="brand-name">BUSTANA</span>
  </div>

  <!-- hero -->
  <div class="abs hero" role="img" aria-label="Fresh tomatoes, peppers, cucumbers and greens around a wicker basket">
    <div class="hero-shade"></div>
    <div class="hero-title">WE ARE A FRUITS &amp; VEGETABLES DISTRIBUTION COMPANY</div>
  </div>

  <div class="abs crumbs"><span>HOME</span>
    <svg width="10" height="5" viewBox="0 0 10 5"><path d="M0 2.5H9M7 .5 9 2.5 7 4.5" stroke="#555" stroke-width=".7" fill="none"/></svg>
    <span class="current">MEDIA COVERAGE</span></div>
  <div class="abs rule"></div>

  <!-- media coverage -->
  <h1 class="abs section-title" style="top:274px;font-weight:400">MEDIA COVERAGE</h1>
  <div class="abs divider" style="top:299px"><span></span>
    <svg width="10" height="11" viewBox="0 0 10 11"><circle cx="5" cy="6.5" r="4" stroke="#333" stroke-width=".8" fill="none"/><path d="M5 2.5V0.5" stroke="#333" stroke-width=".8"/></svg>
    <span></span></div>
  <p class="abs lead">Duis autem vel eum iriure dolor in hendrerit inknl vulputate velit esse molestie consequat, vel illum dolore eumor feugiat nulla facilisis.</p>

  <div class="abs story-thumb" style="top:350px;background:linear-gradient(135deg,#9aa6ad,#b7c0c2 40%,#8a2340 70%,#6e6a5c)" role="img" aria-label="Red apple on a branch">
    <span class="date-day">22 Feb</span><span class="date-year">2016</span></div>
  <div class="abs story-body" style="top:349px">
    <h2 class="story-title">Lorem Ipsum Is Simply Dummy Text Of The Printing And Typesetting Industry</h2>
    <p class="story-text">Lorem Ipsum is simply dummy text of the printing and typesetting industry. Lorem Ipsum has been the industry's standard dummy text ever since the 1500s, when an unknown printer took a galley of type and scrambled it to make a type specimen book. It has survived not only five centuries, but also the leap into electronic typesetting, remaining essentially unchanged.</p>
  </div>

  <div class="abs story-thumb" style="top:437px;background:linear-gradient(135deg,#e9e2cf,#a9b84a 35%,#e0b83c 55%,#c2453a 70%,#7a5430)" role="img" aria-label="Basket of grapes, bananas and peaches">
    <span class="date-day">26 May</span><span class="date-year">2016</span></div>
  <div class="abs story-body" style="top:436px">
    <h2 class="story-title">Lorem Ipsum Is Simply Dummy..</h2>
    <p class="story-text">Lorem Ipsum is simply dummy text of the printing and typesetting industry. Lorem Ipsum has been the industry's standard dummy text ever since the 1500s, when an unknown printer took a galley of type and scrambled it to make a type specimen book. It has survived not only five centuries, but also the leap into electronic typesetting, remaining essentially unchanged.</p>
  </div>

  <div class="abs story-thumb" style="top:523px;background:linear-gradient(135deg,#c8331f,#e98a1e 35%,#6a4a25 55%,#d9a431 80%,#8a6a2a)" role="img" aria-label="Crates of oranges, pineapples and bananas">
    <span class="date-day">01 Jun</span><span class="date-year">2016</span></div>
  <div class="abs story-body" style="top:522px">
    <h2 class="story-title">Lorem Ipsum Is Simply Dummy Text Of.</h2>
    <p class="story-text">Lorem Ipsum is simply dummy text of the printing and typesetting industry. Lorem Ipsum has been the industry's standard dummy text ever since the 1500s, when an unknown printer took a galley of type and scrambled it to make a type specimen book. It has survived not only five centuries, but also the leap into electronic typesetting, remaining essentially unchanged.</p>
  </div>

  <!-- social channels -->
  <h2 class="abs section-title" style="top:635px;font-weight:400">OUR SOCIAL MEDIA CHANNELS</h2>
  <div class="abs divider" style="top:660px"><span></span>
    <svg width="10" height="11" viewBox="0 0 10 11"><circle cx="5" cy="6.5" r="4" stroke="#333" stroke-width=".8" fill="none"/><path d="M5 2.5V0.5" stroke="#333" stroke-width=".8"/></svg>
    <span></span></div>

  <div class="abs channel" style="left:80px"><i></i>FRIENDLINE</div>
  <div class="abs channel" style="left:286px"><i></i>SNAPGRID</div>
  <div class="abs channel" style="left:479px"><i></i>CHIRPER</div>

  <div class="abs fb-box">
    <div class="fb-head">Recent Activity</div>
    <div class="fb-item"><span class="fb-thumb"></span><p><b>Lena Dorr</b> shared <b>Five Ways to Keep Produce Fresh Longer</b> · on Wednesday</p></div>
    <div class="fb-item"><span class="fb-thumb" style="background:#3d6a8a"></span><p><b>Omar Vell</b> shared <b>How Growers Plan the Harvest Season</b> · 2 hours ago</p></div>
    <div class="fb-item"><span class="fb-thumb" style="background:#333"></span><p><b>Tess Kain</b> shared <b>Top 20 Orchard Routes</b> · 4 hours ago</p></div>
    <div class="fb-item"><span class="fb-thumb" style="background:#7a4a3a"></span><p><b>Rui Almas</b> shared <b>Markets Grow Closer To Farms Every Year</b> · about a week ago</p></div>
    <div class="fb-foot">Social feed plugin</div>
  </div>

  <div class="abs ig-profile">
    <span class="ig-avatar"></span>
    <p><span class="ig-handle">@greenroutes</span><br>For 40 years, we have been helping travellers explore the world. Photos by our team and friends on the road.</p>
  </div>
  <div class="abs ig-grid" role="img" aria-label="Grid of twenty travel photographs">
    <div style="background:#7d8f9a"></div><div style="background:#c08850"></div><div style="background:#6e9a5a"></div><div style="background:#50607a"></div>
    <div style="background:#a07040"></div><div style="background:#403530"></div><div style="background:#c0a070"></div><div style="background:#5aa0c0"></div>
    <div style="background:#707070"></div><div style="background:#5ab0b0"></div><div style="background:#605040"></div><div style="background:#a06050"></div>
    <div style="background:#503028"></div><div style="background:#903020"></div><div style="background:#b0b0b0"></div><div style="background:#507050"></div>
    <div style="background:#806050"></div><div style="background:#4a7060"></div><div style="background:#6a8040"></div><div style="background:#a04050"></div>
  </div>
  <div class="abs load-more">Load More...</div>

  <div class="abs tw-box">
    <div class="tw-head">Chirper Feeds <i></i></div>
    <div class="tw-item"><p><b>DevDesk</b> 02nd Dec, 2015<br>Our forums are a great place for more detailed discussion - come chat with us</p><span class="view">View on Chirper</span></div>
    <div class="tw-item"><p><b>DevDesk</b> 02nd Dec, 2015<br>Yes, you can use either the stream or the REST timeline methods for that</p><span class="view">View on Chirper</span></div>
    <div class="tw-item"><p><b>DevDesk</b> 02nd Dec, 2015<br>RT @buildkit: It's official. Introducing build tools for every device today</p><span class="view">View on Chirper</span></div>
    <div class="tw-item"><p><b>DevDesk</b> 02nd Dec, 2015<br>RT @signin: Finally, a login that's seamless on every screen today</p><span class="view">View on Chirper</span></div>
  </div>

  <!-- footer -->
  <div class="abs footer"></div>

  <div class="abs" style="left:80px;top:964px">
    <h3 class="foot-title" style="font-weight:400">CONTACT DETAILS</h3>
    <div class="foot-rule" style="margin-top:7px"></div>
  </div>
  <div class="abs foot-line" style="left:80px;top:999px">
    <svg width="7" height="10" viewBox="0 0 7 10"><path d="M3.5 0A3.5 3.5 0 0 1 7 3.5C7 6 3.5 10 3.5 10S0 6 0 3.5A3.5 3.5 0 0 1 3.5 0Z" fill="#8dc63f"/><circle cx="3.5" cy="3.5" r="1.3" fill="#111"/></svg>
    <p><b style="letter-spacing:.6px;font-weight:600">BUSTANA</b><br>123 euismod cidun ut laoreetmok<br>laoreet dol magnak aliquam</p>
  </div>
  <div class="abs foot-line" style="left:80px;top:1051px">
    <svg width="8" height="8" viewBox="0 0 8 8"><path d="M1.5 0.5 3 0.5 3.6 2.5 2.6 3.3C3.2 4.6 3.9 5.3 4.8 5.6L5.6 4.6 7.5 5.2 7.5 6.8C4 7.2.8 4 1.5.5Z" fill="#8dc63f"/></svg>
    <p>123 456 7890</p>
  </div>
  <div class="abs foot-line" style="left:80px;top:1076px">
    <svg width="8" height="6" viewBox="0 0 8 6"><rect width="8" height="6" rx="1" fill="#8dc63f"/><path d="M0 0 4 3.5 8 0" stroke="#111" stroke-width=".8" fill="none"/></svg>
    <p>info@bustana.com</p>
  </div>
  <div class="abs" style="left:80px;top:1108px">
    <h3 class="foot-title" style="font-weight:400;font-size:10px">FOLLOW US</h3>
    <div class="foot-rule" style="margin-top:6px"></div>
  </div>
  <div class="abs follow-dot" style="left:86px;top:1140px"></div>
  <div class="abs follow-dot" style="left:104px;top:1140px"></div>
  <div class="abs follow-dot" style="left:122px;top:1140px"></div>
  <div class="abs follow-dot" style="left:141px;top:1140px"></div>

  <form class="abs touch">
    <h3>GET IN TOUCH</h3>
    <div class="foot-rule"></div>
    <div class="field">Name</div>
    <div class="field">Email</div>
    <div class="field">Phone</div>
    <div class="field tall">Message</div>
    <div class="submit">SUBMIT</div>
  </form>

  <div class="abs foot-brand">
    <span class="brand-mark"></span>
    <span class="brand-name">BUSTANA</span>
  </div>

  <div class="abs copybar">Copyright © 2018 BUSTANA . All Right Reserved.</div>
</div>
</body>
</html>
```